Business Card Design Project

A polished, very professional looking business card. I think we want to keep it all grey. I've attached our old logo, and current mockup in which case we really like the font.

Target Market(s)

Target Market are Bride and Grooms and Wedding Coordinators. We are wedding photographers

Industry/Entity Type

Business

Font styles to use
Serif
Sans Serif

Requirements
Must have
• An elegant, yet simple and sophisticated appearance.

Phone number, Email, Website and Social Media link.
Nice to have
• An element that can be spot glossed when printed. Not necessary though.
Should not have
• Bright colors, images or intensive graphics.

```html
<!DOCTYPE html>
<html lang="en">
<head>
<meta charset="utf-8">
<title>Wesley Marlowe Photographers – Business Card</title>
<link rel="stylesheet" href="https://fonts.googleapis.com/css2?family=Josefin+Sans:wght@300;400&display=swap">
<style>
  :root {
    --backdrop: #cfcdca;
    --card: #0d0d0d;
    --ink: #f2f2f2;
    --ink-soft: #c9c9c9;
    --rule: #9a9a9a;
  }
  * { box-sizing: border-box; margin: 0; padding: 0; }
  html, body { width: 1200px; height: 873px; overflow: hidden; }
  body {
    background: var(--backdrop);
    font-family: "Josefin Sans", Arial, sans-serif;
    position: relative;
  }
  .card {
    position: absolute;
    top: 174px;
    width: 300px;
    height: 525px;
    background: var(--card);
    border-radius: 3px;
    box-shadow: 0 10px 28px rgba(0,0,0,0.28);
    overflow: hidden;
  }
  .card--back { left: 250px; }
  .card--front { left: 650px; }

  /* content laid out landscape, turned to read top-to-bottom */
  .card__face {
    position: absolute;
    left: -112.5px;
    top: 112.5px;
    width: 525px;
    height: 300px;
    transform: rotate(90deg);
  }

  .contact {
    position: absolute;
    left: 120px;
    top: 44px;
    display: flex;
    align-items: stretch;
  }
  .contact__labels {
    text-align: right;
    color: var(--ink);
    font-weight: 400;
    font-size: 13px;
    letter-spacing: 0.06em;
    line-height: 18px;
    padding-right: 12px;
  }
  .contact__divider {
    width: 1px;
    background: var(--rule);
  }
  .contact__values {
    color: var(--ink-soft);
    font-weight: 300;
    font-size: 14.5px;
    letter-spacing: 0.02em;
    line-height: 18px;
    padding-left: 12px;
  }

  .brand {
    position: absolute;
    left: 0;
    top: 56px;
    width: 525px;
    display: flex;
    flex-direction: column;
    align-items: center;
  }
  .brand__mark {
    width: 36px;
    height: 36px;
    background: var(--ink);
    margin-bottom: 14px;
  }
  .brand__name {
    color: var(--ink);
    font-weight: 400;
    font-size: 21px;
    letter-spacing: 0.28em;
    white-space: nowrap;
    padding-left: 0.28em;
  }
  .brand__rule {
    width: 26px;
    height: 1px;
    background: var(--rule);
    margin: 8px auto 6px;
  }
  .brand__tagline {
    color: var(--ink-soft);
    font-weight: 300;
    font-size: 9px;
    letter-spacing: 0.5em;
    padding-left: 0.5em;
  }
</style>
</head>
<body>
  <section class="card card--back" aria-label="Card back, contact details">
    <div class="card__face">
      <div class="contact">
        <div class="contact__labels">
          <p>PHONE</p>
          <p>WEBSITE</p>
          <p>EMAIL</p>
          <p>SOCIAL</p>
        </div>
        <div class="contact__divider"></div>
        <div class="contact__values">
          <p>555.214.3907</p>
          <p>www.wesleymarlowe.com</p>
          <p>wes@wesleymarlowe.com</p>
          <p>WesleyMarlowePhoto</p>
        </div>
      </div>
    </div>
  </section>

  <section class="card card--front" aria-label="Card front, studio name">
    <div class="card__face">
      <div class="brand">
        <div class="brand__mark"></div>
        <p class="brand__name">WESLEY MARLOWE</p>
        <div class="brand__rule"></div>
        <p class="brand__tagline">PHOTOGRAPHERS</p>
      </div>
    </div>
  </section>
</body>
</html>
```